Courier Business needs a Business Card Design !!!

My new company needs a business card design. Our company name is Maple Dart Courier & Delivery Services. We will be servicing residential , government and business clients in the City of Yellowknife, Northwest Territories, Canada. I would like the following information included on the card: Name- Calvin Oxley. Title- Owner. Company- Maple Dart Courier & Delivery Services. Address- PO Box 5918 , Yellowknife , NWT, X0E 4K3. Phone- 867-555-0193. Email- mapledartdelivery@postfern.example. Facebook- www.socialpage.example/mapledartdelivery. I would like my double sided card to be the standard size of 84mm x 55mm. No borders. Use CMYK mode.1039x 697 pixels at least. I would like my logo to take up at least one quarter of the area of one side of the card. Text should be at least 8 point with perhaps my name being 10 point and my company name being 12-15 point . It should have clear readable font. Please use one or two bold colors. I am trying to attract the business community so a professional look might be best. My tag line is " On Time Every Time ". Nice safe margins please. We will be providing fast, reliable and professional delivery of envelopes and small packages within the City of Yellowknife. We offer 100% satisfaction or a complete refund. I have included a file of our logo. I like black, blue and red but am willing to look at what you feel would work best. I do not really like white as a background color.

Target Market(s)

Professionals , business owners. 30-50 years old

Industry/Entity Type

Residential

Contact Information for Business Card

As noted in brief

Font styles to use
Serif
Sans Serif

Colors
000000
0255a3
f04a50

Requirements
Must have
• My contact info. My logo
Nice to have
• Simple elegant design but still catches the eye
Should not have
• White background color

```html
<!DOCTYPE html>
<html lang="en">
<head>
<meta charset="utf-8">
<title>Maple Dart Courier &amp; Delivery Services – Business Card</title>
<link rel="stylesheet" href="https://fonts.googleapis.com/css2?family=Russo+One&family=Exo+2:wght@400;700;800&family=Antonio:wght@200&display=swap">
<style>
  :root {
    --backdrop: #5a5a5a;
    --card-mat: #ffffff;
    --card-ink: #231f20;
    --brand-red: #f04a50;
    --text-light: #ffffff;
  }
  * { margin: 0; padding: 0; box-sizing: border-box; }
  html, body { width: 1200px; height: 1000px; overflow: hidden; }
  body { background: var(--backdrop); position: relative; font-family: "Exo 2", sans-serif; }

  .card-mat { position: absolute; top: 127px; width: 500px; height: 763px; background: var(--card-mat); }
  .card-mat.front { left: 95px; }
  .card-mat.back { left: 615px; }
  .card {
    position: absolute; left: 27px; top: 27px; width: 446px; height: 708px;
    background: var(--card-ink); border-radius: 12px; overflow: hidden;
  }

  /* front */
  .holder-name {
    position: absolute; left: 104px; top: 88px; width: 260px;
    font-family: "Russo One", sans-serif; font-size: 60px; line-height: 62px;
    color: var(--brand-red); transform: rotate(-3deg); text-align: center;
  }
  .holder-title {
    position: absolute; left: 0; width: 446px; top: 248px; text-align: center;
    font-family: "Russo One", sans-serif; font-size: 28px; color: var(--text-light);
  }
  .speed-art { position: absolute; left: 0; top: 280px; }
  .phone-tag {
    position: absolute; left: 59px; top: 473px; width: 322px; height: 52px;
    background: var(--brand-red); border-radius: 5px;
    font-family: "Russo One", sans-serif; font-size: 25px; color: var(--card-ink);
    display: flex; align-items: center; justify-content: center;
  }
  .contact-lines {
    position: absolute; left: 0; width: 446px; top: 620px; text-align: center;
    font-size: 19px; line-height: 32px; color: var(--text-light);
  }

  /* back */
  .wordmark {
    position: absolute; left: 40px; top: 150px; width: 366px; height: 180px;
    display: flex; align-items: center; justify-content: center; gap: 14px;
  }
  .wordmark-square { width: 26px; height: 26px; background: var(--brand-red); flex: none; }
  .wordmark-name {
    font-family: "Exo 2", sans-serif; font-weight: 800; font-size: 30px; line-height: 34px;
    color: var(--text-light); text-transform: uppercase;
  }
  .company-name {
    position: absolute; left: 0; width: 446px; top: 449px; text-align: center;
    font-size: 24px; line-height: 32px; color: var(--text-light);
  }
  .postal-address {
    position: absolute; left: 0; width: 446px; top: 543px; text-align: center;
    font-size: 24px; line-height: 32px; color: var(--brand-red);
  }
  .tagline-band {
    position: absolute; left: 0; top: 662px; width: 446px; height: 29px;
    background: var(--brand-red); overflow: visible;
  }
  .tagline {
    position: absolute; left: 0; width: 446px; top: -10px; text-align: center;
    font-family: "Antonio", sans-serif; font-weight: 200; font-size: 40px; line-height: 46px;
    color: var(--card-ink); white-space: nowrap;
  }
</style>
</head>
<body>
  <section class="card-mat front">
    <div class="card">
      <h1 class="holder-name">Calvin Oxley</h1>
      <p class="holder-title">owner</p>
      <svg class="speed-art" width="446" height="120" viewBox="0 0 446 120">
        <rect role="img" aria-label="Running bird illustration leaving the left edge" x="0" y="3" width="84" height="100" rx="18" fill="#ffffff"/>
        <line x1="52" y1="12" x2="330" y2="10" stroke="#ffffff" stroke-width="2"/>
        <line x1="170" y1="18" x2="330" y2="17" stroke="#ffffff" stroke-width="1.5"/>
        <line x1="230" y1="25" x2="330" y2="24" stroke="#ffffff" stroke-width="1.5"/>
        <rect role="img" aria-label="Running bird illustration entering from the right edge" x="318" y="3" width="128" height="118" rx="22" fill="#ffffff"/>
      </svg>
      <div class="phone-tag">Phone- 867-555-0193</div>
      <div class="contact-lines">
        <p>mapledartdelivery@postfern.example</p>
        <p>socialpage.example/mapledartdelivery</p>
      </div>
    </div>
  </section>

  <section class="card-mat back">
    <div class="card">
      <div class="wordmark">
        <span class="wordmark-square"></span>
        <span class="wordmark-name">Maple Dart<br>Courier &amp; Delivery<br>Services</span>
      </div>
      <p class="company-name">Maple Dart<br>Courier &amp; Delivery Services</p>
      <p class="postal-address">PO Box 5918 , Yellowknife<br>NWT, X0E 4K3</p>
      <div class="tagline-band"><p class="tagline">ON TIME EVERY TIME</p></div>
    </div>
  </section>
</body>
</html>
```